Design for a 3-4 screens mobile app

The app is a "simple" ordering mobile app.
1. START screen : user can select either "NEW order" either "VIEW history" - or, can access the usual Contact, About, and Conditions pages.
2. NEW order : is a sequence of 3 basic screens/forms made of 3-4 fields each. Logic is the following: you select the service you need, its recurrence, mention where you are located and then you post it towards the marketplace...
3. VIEW history : is where you land at the end of the ordering process - and accessible from START screen. You see there your previous orders, and their statuses.
Mandatory : we need design for START screen, NEW order and VIEW history screens.
Design but be optimized for Smartphones, used in Portrait mode.
Please take into account the design of the website promoting the Mobile App: https://tidyvanlane.be/
Optional but of course nice to have if you could propose some design or guidance for Contact, About, and Conditions pages...
Here attached a full screen sequence.
Updates
Thanks for all your proposals ! They were submitted to the final customer, he selects one ASAP !
Number of Pages Required
3 page
Look and feel
Each slider illustrates characteristics of the customer's brand and the style your logo design should communicate.

```html
<!DOCTYPE html>
<html lang="en">
<head>
<meta charset="utf-8">
<title>Tidy van Lane – New order summary</title>
<link href="https://fonts.googleapis.com/css2?family=Montserrat:wght@400;500;600;700&display=swap" rel="stylesheet">
<style>
  :root{
    --orange:#e8691f;
    --orange-deep:#d65718;
    --orange-light:#ee7628;
    --header:#d95b17;
    --icon-disc:rgba(120,40,0,.32);
    --divider:rgba(255,255,255,.32);
    --white:#ffffff;
    --ink:#1b1b1b;
  }
  *{box-sizing:border-box;margin:0;padding:0}
  html,body{width:675px;height:1200px;overflow:hidden;background:#fff}
  body{font-family:'Montserrat',sans-serif;color:var(--white)}
  .screen{position:relative;width:675px;height:1200px;overflow:hidden;background:var(--orange)}
  .backdrop{position:absolute;left:0;top:140px;width:675px;height:1060px;
    background:linear-gradient(170deg,var(--orange-light) 0%,var(--orange) 50%,var(--orange-deep) 100%)}
  .status-bar{position:absolute;top:0;left:0;width:675px;height:40px;background:var(--white);
    color:var(--ink);font-family:-apple-system,'Helvetica Neue',Arial,sans-serif;font-size:26px;font-weight:600}
  .status-bar .carrier{position:absolute;left:12px;top:5px;font-weight:400;display:flex;align-items:center;gap:8px}
  .status-bar .time{position:absolute;left:0;right:0;top:5px;text-align:center}
  .status-bar .battery{position:absolute;right:12px;top:9px}
  .top-bar{position:absolute;top:40px;left:0;width:675px;height:100px;background:var(--header)}
  .back-button{position:absolute;left:56px;top:10px;width:72px;height:72px;background:var(--white);
    color:var(--orange);display:flex;flex-direction:column;align-items:center;justify-content:center;gap:3px;
    font-size:12px;font-weight:700;letter-spacing:.5px}
  .step-icon{position:absolute;top:22px}
  .order-list{position:absolute;left:140px;top:170px;width:450px;list-style:none}
  .order-item{position:relative;height:117.5px;display:flex;align-items:center;
    border-bottom:2px solid var(--divider)}
  .order-item:first-child{height:117px}
  .item-icon{position:absolute;left:4px;width:68px;height:68px;border-radius:50%;background:var(--icon-disc);
    display:flex;align-items:center;justify-content:center}
  .item-text{margin-left:80px;line-height:1.25}
  .label{font-size:19px;font-weight:600;letter-spacing:.3px}
  .label.small{font-weight:500}
  .value{font-size:32px;font-weight:500;letter-spacing:.5px}
  .value.small{font-size:19px;font-weight:500}
  .lead{font-size:24px;font-weight:500}
  .lead strong{font-weight:700}
  .send-button{position:absolute;left:140px;top:1024px;width:393px;height:58px;background:var(--white);
    color:var(--orange-deep);border:none;font-family:'Montserrat',sans-serif;font-size:20px;font-weight:600;
    letter-spacing:.5px}
</style>
</head>
<body>
<main class="screen">
  <div class="backdrop" role="img" aria-label="Faceted orange low-poly background"></div>

  <header class="status-bar">
    <span class="carrier">Carrier
      <svg width="24" height="18" viewBox="0 0 24 18"><path d="M12 17l-3-3a4 4 0 0 1 6 0zM5 10a10 10 0 0 1 14 0l-2 2a7 7 0 0 0-10 0zM1 6a16 16 0 0 1 22 0l-2 2a13 13 0 0 0-18 0z" fill="#1b1b1b"/></svg>
    </span>
    <span class="time">2:32 PM</span>
    <svg class="battery" width="56" height="24" viewBox="0 0 56 24"><rect x="1" y="1" width="48" height="22" rx="5" fill="none" stroke="#1b1b1b" stroke-width="2"/><rect x="4" y="4" width="42" height="16" rx="3" fill="#1b1b1b"/><rect x="51" y="8" width="4" height="8" rx="2" fill="#1b1b1b"/></svg>
  </header>

  <nav class="top-bar">
    <div class="back-button">
      <svg width="34" height="34" viewBox="0 0 34 34"><circle cx="17" cy="17" r="16" fill="var(--orange)"/><path d="M19 9l-8 8 8 8M11 17h14" stroke="#fff" stroke-width="3.5" fill="none" stroke-linecap="round" stroke-linejoin="round"/></svg>
      BACK
    </div>
    <svg class="step-icon" style="left:290px" width="50" height="50" viewBox="0 0 50 50"><path d="M25 3l19 11v22L25 47 6 36V14z" fill="none" stroke="rgba(255,255,255,.55)" stroke-width="2"/><path d="M25 19v12M19 25h12" stroke="rgba(255,255,255,.55)" stroke-width="2"/></svg>
    <svg class="step-icon" style="left:391px" width="50" height="50" viewBox="0 0 50 50"><path d="M25 3l19 11v22L25 47 6 36V14z" fill="none" stroke="rgba(255,255,255,.55)" stroke-width="2"/><rect x="15" y="18" width="16" height="14" fill="none" stroke="rgba(255,255,255,.55)" stroke-width="2"/><path d="M19 18v-3h16v14h-4" fill="none" stroke="rgba(255,255,255,.55)" stroke-width="2"/></svg>
  </nav>

  <ul class="order-list">
    <li class="order-item">
      <span class="item-icon"><svg width="40" height="30" viewBox="0 0 40 30"><path d="M4 24h32c0-9-6-15-16-15h-8" fill="none" stroke="#fff" stroke-width="2.5" stroke-linejoin="round"/><path d="M10 9c0-4 4-5 8-5h10" fill="none" stroke="#fff" stroke-width="2.5" stroke-linecap="round"/><path d="M8 18h20" stroke="#fff" stroke-width="2"/></svg></span>
      <div class="item-text"><p class="lead">I need <strong>IRONING</strong></p></div>
    </li>
    <li class="order-item">
      <span class="item-icon"><svg width="36" height="36" viewBox="0 0 36 36"><circle cx="18" cy="18" r="15" fill="none" stroke="#fff" stroke-width="2.5"/><path d="M18 9v9l7 5" fill="none" stroke="#fff" stroke-width="2.5" stroke-linecap="round"/></svg></span>
      <div class="item-text"><p class="lead">For 4 hours</p></div>
    </li>
    <li class="order-item">
      <span class="item-icon"><svg width="36" height="36" viewBox="0 0 36 36"><path d="M31 15A14 14 0 1 0 31 22" fill="none" stroke="#fff" stroke-width="2.5" stroke-linecap="round"/><path d="M26 14h6V8" fill="none" stroke="#fff" stroke-width="2.5" stroke-linecap="round" stroke-linejoin="round"/><path d="M17 11v8l5 3" fill="none" stroke="#fff" stroke-width="2.5" stroke-linecap="round"/></svg></span>
      <div class="item-text"><p class="label small">Frequency</p><p class="value small">On a weekly basis</p></div>
    </li>
    <li class="order-item">
      <span class="item-icon"><svg width="38" height="38" viewBox="0 0 38 38"><path d="M8 4l6 1 3 8-4 3c2 5 5 8 10 10l3-4 8 3 1 6c-1 3-4 4-7 3C17 31 8 22 5 11c-1-3 0-6 3-7z" fill="none" stroke="#fff" stroke-width="2.3" stroke-linejoin="round"/><path d="M22 10l3 3 6-7" fill="none" stroke="#fff" stroke-width="2.3" stroke-linecap="round" stroke-linejoin="round"/></svg></span>
      <div class="item-text"><p class="label">CALL ME ON</p><p class="value">0470 55 21 84</p></div>
    </li>
    <li class="order-item">
      <span class="item-icon"><svg width="36" height="36" viewBox="0 0 36 36" fill="none" stroke="#fff" stroke-width="2"><circle cx="8" cy="8" r="3.5"/><circle cx="18" cy="8" r="3.5"/><circle cx="28" cy="8" r="3.5"/><circle cx="8" cy="18" r="3.5"/><circle cx="18" cy="18" r="3.5"/><circle cx="28" cy="18" r="3.5"/><circle cx="8" cy="28" r="3.5"/><circle cx="18" cy="28" r="3.5"/><circle cx="28" cy="28" r="3.5"/></svg></span>
      <div class="item-text"><p class="label">Mealpass client number</p><p class="value">123456789555</p></div>
    </li>
    <li class="order-item">
      <span class="item-icon"><svg width="38" height="32" viewBox="0 0 38 32" fill="none" stroke="#fff" stroke-width="2.3" stroke-linejoin="round"><path d="M3 6h32v6a4 4 0 0 0 0 8v6H3v-6a4 4 0 0 0 0-8z"/><path d="M10 12h18M10 16h18M10 20h12"/></svg></span>
      <div class="item-text"><p class="label">VAUCHER FORMAT</p><p class="value small">Papier</p></div>
    </li>
    <li class="order-item">
      <span class="item-icon"><svg width="30" height="38" viewBox="0 0 30 38" fill="none" stroke="#fff" stroke-width="2.5"><path d="M15 36S3 22 3 14a12 12 0 0 1 24 0c0 8-12 22-12 22z" stroke-linejoin="round"/><circle cx="15" cy="14" r="4.5"/></svg></span>
      <div class="item-text"><p class="label">AT THIS ADDRESS</p><p class="value small">Rue des Tilleuls 8, 1050 Ixelles</p></div>
    </li>
  </ul>

  <button class="send-button" type="button">SEND REQUEST</button>
</main>
</body>
</html>
```